Transformative School Model Needs a Website. I am easy to work with.

Greetings:
I am creating a K-12 school that is a complete and total re-imagination of what education can be for children, families, communities, and the planet. While we will begin as a K-12 school, I really see it as a complete life cycle education (birth to death). I'm looking for a website to describe my new transformational educational model. I anticipate having 7-8 pages. I have all the copy ready.
I am the Founder. I am easy to work with, an effective communicator, and I’m very good at knowing what I want and providing specific and concrete detail, examples, and direction to make sure I use your time wisely.

```html
<!DOCTYPE html>
<html lang="en">
<head>
<meta charset="utf-8">
<title>Serene Path Academy</title>
<link href="https://fonts.googleapis.com/css2?family=Poppins:wght@400;500;600;700&display=swap" rel="stylesheet">
<style>
:root{
  --blue:#48a7d3;
  --orange:#f8a100;
  --ink:#2b2b2b;
  --text:#4a4a4a;
  --grey-bg:#f0f0f0;
  --soft-bg:#f7f7f7;
  --foot-bg:#ececec;
  --white:#ffffff;
}
*{box-sizing:border-box;margin:0;padding:0}
html,body{width:1200px;height:5051px;overflow:hidden}
body{font-family:'Poppins',sans-serif;color:var(--text);background:var(--white);position:relative}
.abs{position:absolute}
.btn{position:absolute;background:var(--orange);color:var(--white);display:flex;align-items:center;justify-content:center;font-weight:500}
.photo{position:absolute}

/* top bar + nav */
.topbar{position:absolute;left:0;top:0;width:1200px;height:31px;background:var(--blue)}
.topbar .contact{position:absolute;left:900px;top:0;line-height:31px;font-size:13px;color:var(--white)}
.topbar .donate{position:absolute;left:1004px;top:0;width:112px;height:31px;background:var(--orange);color:var(--white);font-size:13px;text-align:center;line-height:31px}
.brand{position:absolute;left:88px;top:31px;height:79px;display:flex;align-items:center;gap:10px;font-size:15px;font-weight:600;color:var(--blue)}
.brand .dot{width:18px;height:18px;border-radius:50%;background:var(--orange)}
.nav{position:absolute;right:85px;top:31px;height:79px;display:flex;align-items:center;gap:24px;font-size:13px;color:var(--text)}
.nav .caret::after{content:"";display:inline-block;margin-left:5px;border:4px solid transparent;border-top:5px solid #888;vertical-align:-2px}

/* hero */
.hero{position:absolute;left:0;top:110px;width:1200px;height:578px;background:linear-gradient(120deg,#3b3a36 0%,#6d6759 45%,#4b4a43 70%,#2f3a2e 100%)}
.hero::after{content:"";position:absolute;inset:0;background:rgba(0,0,0,.35)}
.hero h1{position:absolute;z-index:1;left:0;width:1200px;top:172px;text-align:center;color:var(--white);font-size:38px;line-height:51px;font-weight:700;text-transform:uppercase}
.hero p{position:absolute;z-index:1;left:0;width:1200px;top:302px;text-align:center;color:var(--white);font-size:15px;line-height:26px}
.hero .btn{z-index:1;left:502px;top:396px;width:196px;height:72px;font-size:20px}

/* welcome */
.seal{position:absolute;left:88px;top:790px;width:422px;height:420px}
.seal-name{position:absolute;left:88px;top:985px;width:422px;text-align:center;font-size:26px;font-weight:600;color:var(--ink)}
.welcome .kicker{position:absolute;left:573px;top:810px;font-size:19px;color:var(--blue);text-transform:uppercase}
.welcome h2{position:absolute;left:573px;top:836px;font-size:30px;font-weight:700;color:var(--blue);text-transform:uppercase}
.welcome p{position:absolute;left:573px;top:894px;width:490px;font-size:15px;line-height:31px;color:var(--ink)}
.welcome .btn{left:573px;top:1170px;width:158px;height:46px;font-size:15px}

/* curriculum */
.curriculum{position:absolute;left:0;top:1306px;width:1200px;height:1573px;background:var(--grey-bg)}
.section-title{position:absolute;left:0;width:1200px;text-align:center;font-size:30px;font-weight:600;color:var(--blue);text-transform:uppercase}
.activity{position:absolute;width:500px;text-align:center}
.activity .photo{left:0;top:0;width:500px;height:343px}
.activity h3{position:absolute;left:0;top:362px;width:500px;font-size:24px;font-weight:500;color:var(--blue);text-transform:uppercase}
.activity p{position:absolute;left:40px;top:405px;width:420px;font-size:15px;line-height:26px;color:var(--text)}
.activity .btn{left:181px;top:537px;width:139px;height:51px;font-size:14px}

/* donate banner */
.banner{position:absolute;left:0;top:2879px;width:1200px;height:525px;background:linear-gradient(110deg,#3a4a52,#6b6a5c 40%,#7a6a55 65%,#3f4b44)}
.banner::after{content:"";position:absolute;inset:0;background:rgba(0,0,0,.45)}
.banner h2{position:absolute;z-index:1;left:0;width:1200px;top:135px;text-align:center;font-size:30px;font-weight:600;color:var(--white);text-transform:uppercase}
.banner p{position:absolute;z-index:1;left:175px;width:850px;top:195px;text-align:center;font-size:15px;line-height:26px;color:var(--white)}
.banner .btn{z-index:1;left:480px;top:313px;width:251px;height:87px;font-size:20px;font-weight:600;text-transform:uppercase}

/* program tiles */
.tile{position:absolute;top:3494px;width:318px;height:369px}
.tile .photo{left:0;top:0;width:318px;height:296px}
.tile .label{position:absolute;left:0;top:296px;width:318px;height:73px;background:var(--blue);color:var(--white);display:flex;align-items:center;justify-content:center;font-size:16px;font-weight:500;text-transform:uppercase}

/* testimonials */
.testimonials{position:absolute;left:0;top:3941px;width:1200px;height:745px;background:var(--soft-bg)}
.quote{position:absolute;width:480px;height:200px}
.quote .avatar{position:absolute;left:0;top:0;width:112px;height:112px;border-radius:50%;background:linear-gradient(160deg,#d9d2c8,#9a8f84)}
.quote .mark{position:absolute;left:122px;top:-40px;font-size:42px;line-height:1;color:#666;font-family:Georgia,serif}
.quote .mark.end{left:256px;top:88px}
.quote p{position:absolute;left:142px;top:-5px;width:305px;font-size:14px;line-height:20.5px;color:var(--text)}
.quote .name{position:absolute;left:142px;top:125px;font-size:14px;font-weight:600;color:var(--ink)}
.quote .role{position:absolute;left:142px;top:147px;font-size:10px;color:var(--text)}
.quote .stars{position:absolute;left:142px;top:160px;font-size:14px;letter-spacing:1px;color:var(--orange)}

/* footer */
.footer{position:absolute;left:0;top:4686px;width:1200px;height:279px;background:var(--foot-bg)}
.footer .f-brand{position:absolute;left:160px;top:110px;display:flex;align-items:center;gap:8px;font-size:15px;font-weight:600;color:var(--blue)}
.footer .f-brand .dot{width:14px;height:14px;border-radius:50%;background:var(--orange)}
.footer h4{position:absolute;top:68px;font-size:13px;font-weight:500;color:var(--blue)}
.links{position:absolute;left:331px;top:98px;list-style:none;font-size:11px;line-height:20.5px;color:var(--text)}
.links li::before{content:"";display:inline-block;width:6px;height:6px;border-radius:50%;background:var(--blue);margin-right:10px;vertical-align:1px}
.contact-line{position:absolute;left:500px;display:flex;gap:8px;font-size:11px;line-height:14px;color:var(--text)}
.about-text{position:absolute;left:720px;top:100px;width:335px;font-size:11px;line-height:20px;color:var(--text)}
.subscribe{position:absolute;left:720px;top:187px;width:329px;height:45px;background:var(--white);border:1px solid #ddd}
.subscribe span{position:absolute;left:12px;top:14px;font-size:11px;color:#999}
.subscribe b{position:absolute;right:10px;top:11px;width:58px;height:23px;background:var(--blue);color:var(--white);font-size:10px;font-weight:600;display:flex;align-items:center;justify-content:center}
.bottombar{position:absolute;left:0;top:4965px;width:1200px;height:86px;background:var(--blue)}
.bottombar .copy{position:absolute;left:88px;top:35px;font-size:11px;color:var(--white)}
.social{position:absolute;left:990px;top:32px;display:flex;gap:5px}
.social span{width:22px;height:22px;border-radius:50%;border:1.5px solid var(--white)}
</style>
</head>
<body>

<header>
  <div class="topbar">
    <span class="contact">Contact</span>
    <span class="donate">Donate</span>
  </div>
  <div class="brand"><span class="dot"></span>Serene Path Academy</div>
  <nav class="nav">
    <span class="caret">About</span>
    <span class="caret">School Foundation</span>
    <span class="caret">Curriculum</span>
    <span class="caret">Pedagogy</span>
    <span class="caret">Outcomes</span>
    <span>Opening</span>
    <span>Testimonials</span>
  </nav>
</header>

<section class="hero" role="img" aria-label="Carved stone temple lantern in a garden">
  <h1>Sit nemo reprehenderit eos molestias<br>repudiandae vel</h1>
  <p>Lorem ipsum is placeholder text commonly used in the graphic, print, and publishing<br>industries for previewing layouts and visual mockups.</p>
  <span class="btn">Read More</span>
</section>

<section class="welcome">
  <svg class="seal" viewBox="0 0 422 420" aria-hidden="true"><circle cx="211" cy="210" r="205" fill="none" stroke="#1a1a1a" stroke-width="5"/></svg>
  <div class="seal-name">Serene Path Academy</div>
  <div class="kicker">Welcome to</div>
  <h2>Serene Path Academy</h2>
  <p>Lorem ipsum dolor sit amet, consectetur adipiscing elit, sed do eiusmod tempor incididunt ut labore et dolore magna aliqua. Ut enim ad minim veniam, quis nostrud exercitation ullamco laboris nisi ut aliquip ex ea commodo consequat. Duis aute irure dolor in reprehenderit in voluptate velit esse cillum dolore eu fugiat nulla pariatur. Excepteur sint occaecat cupidatat non proident, sunt in culpa qui officia deserunt mollit anim id est laborum.</p>
  <span class="btn">Read More</span>
</section>

<section class="curriculum">
  <h2 class="section-title" style="top:96px">Curriculum Activities</h2>

  <article class="activity" style="left:86px;top:210px">
    <div class="photo" role="img" aria-label="Students painting at easels in an art room" style="background:linear-gradient(135deg,#e8e6e2,#c9b7a4 55%,#a2503f)"></div>
    <h3>Creative Expression</h3>
    <p>Lorem ipsum dolor sit amet. At dicta totam sit omnis maiores eum voluptatem ullam eum galisum consequuntur. Et reiciendis officiis qui temporibus delectus id odit quia est adipisci doloribus et pariatur</p>
    <span class="btn">Read More</span>
  </article>

  <article class="activity" style="left:614px;top:210px">
    <div class="photo" role="img" aria-label="Martial arts group training outdoors" style="background:linear-gradient(180deg,#c4d2dc,#9aa7ae 55%,#3a3a3a)"></div>
    <h3>Martial Arts</h3>
    <p>Lorem ipsum dolor sit amet. At dicta totam sit omnis maiores eum voluptatem ullam eum galisum consequuntur. Et reiciendis officiis qui temporibus delectus id odit quia est adipisci doloribus et pariatur</p>
    <span class="btn">Read More</span>
  </article>

  <article class="activity" style="left:86px;top:878px">
    <div class="photo" role="img" aria-label="Young children playing football on a grass pitch" style="background:linear-gradient(180deg,#4e7b3c,#3f8a2a 45%,#46a12d)"></div>
    <h3>Sports</h3>
    <p>Lorem ipsum dolor sit amet. At dicta totam sit omnis maiores eum voluptatem ullam eum galisum consequuntur. Et reiciendis officiis qui temporibus delectus id odit quia est adipisci doloribus et pariatur</p>
    <span class="btn">Read More</span>
  </article>

  <article class="activity" style="left:614px;top:878px">
    <div class="photo" role="img" aria-label="Teacher and child kneeling in a quiet practice hall" style="background:linear-gradient(180deg,#e9e7e3,#c8bfb3 60%,#7a5438)"></div>
    <h3>Meditation</h3>
    <p>Lorem ipsum dolor sit amet. At dicta totam sit omnis maiores eum voluptatem ullam eum galisum consequuntur. Et reiciendis officiis qui temporibus delectus id odit quia est adipisci doloribus et pariatur</p>
    <span class="btn">Read More</span>
  </article>
</section>

<section class="banner" role="img" aria-label="Smiling students together in a classroom">
  <h2>Qui aspernatur perspiciatis ab officia dicta est</h2>
  <p>Et ipsum exercitationem sed nihil explicabo rem beatae perferendis! Aut officia quis et totam possimus et neque consequuntur. Et modi dolor et expedita nostrum aut libero ducimus. Sed nobis nisi vel numquam totam in dolores ducimus.</p>
  <span class="btn">Donate Now</span>
</section>

<section class="programs">
  <div class="tile" style="left:86px">
    <div class="photo" role="img" aria-label="Girl writing on a chalkboard" style="background:linear-gradient(135deg,#e6e1dc,#b9b4b0 50%,#d7476b)"></div>
    <div class="label">Quo molestiae deleniti</div>
  </div>
  <div class="tile" style="left:441px">
    <div class="photo" role="img" aria-label="Pupils seated at desks in a classroom" style="background:linear-gradient(180deg,#ece9e3,#c9b8a0 55%,#8c6b4d)"></div>
    <div class="label">Vel deleniti molestiae</div>
  </div>
  <div class="tile" style="left:798px">
    <div class="photo" role="img" aria-label="Boy working on a worksheet in class" style="background:linear-gradient(160deg,#e8e4df,#cbc3ba 50%,#2f9a5a)"></div>
    <div class="label">Lorem ipsum dolor sit</div>
  </div>
</section>

<section class="testimonials">
  <h2 class="section-title" style="top:88px">Clients Testimonials</h2>

  <figure class="quote" style="left:148px;top:213px">
    <div class="avatar" role="img" aria-label="Portrait of the reviewer"></div>
    <span class="mark">&ldquo;</span>
    <p>Lorem ipsum, or lipsum as it is sometimes known, is dummy text used in laying out print, graphic or web designs. The passage is attributed to an unknown typesetter in the 15th century</p>
    <span class="mark end">&rdquo;</span>
    <div class="name">Mara Ellison</div>
    <div class="role">CEO, Northfield Co.</div>
    <div class="stars">★★★★★</div>
  </figure>

  <figure class="quote" style="left:618px;top:213px">
    <div class="avatar" role="img" aria-label="Portrait of the reviewer"></div>
    <span class="mark">&ldquo;</span>
    <p>Lorem ipsum, or lipsum as it is sometimes known, is dummy text used in laying out print, graphic or web designs. The passage is attributed to an unknown typesetter in the 15th century</p>
    <span class="mark end">&rdquo;</span>
    <div class="name">Mara Ellison</div>
    <div class="role">CEO, Northfield Co.</div>
    <div class="stars">★★★★★</div>
  </figure>

  <figure class="quote" style="left:148px;top:497px">
    <div class="avatar" role="img" aria-label="Portrait of the reviewer"></div>
    <span class="mark">&ldquo;</span>
    <p>Lorem ipsum, or lipsum as it is sometimes known, is dummy text used in laying out print, graphic or web designs. The passage is attributed to an unknown typesetter in the 15th century</p>
    <span class="mark end">&rdquo;</span>
    <div class="name">Mara Ellison</div>
    <div class="role">CEO, Northfield Co.</div>
    <div class="stars">★★★★★</div>
  </figure>

  <figure class="quote" style="left:620px;top:497px">
    <div class="avatar" role="img" aria-label="Portrait of the reviewer"></div>
    <span class="mark">&ldquo;</span>
    <p>Lorem ipsum, or lipsum as it is sometimes known, is dummy text used in laying out print, graphic or web designs. The passage is attributed to an unknown typesetter in the 15th century</p>
    <span class="mark end">&rdquo;</span>
    <div class="name">Mara Ellison</div>
    <div class="role">CEO, Northfield Co.</div>
    <div class="stars">★★★★★</div>
  </figure>
</section>

<footer class="footer">
  <div class="f-brand"><span class="dot"></span>Serene Path Academy</div>

  <h4 style="left:331px">Quick Links</h4>
  <ul class="links">
    <li>Home</li><li>About Us</li><li>Openings</li><li>Donate</li><li>Latest News</li><li>Testimonials</li><li>Contact Us</li>
  </ul>

  <h4 style="left:500px">Contact Us</h4>
  <div class="contact-line" style="top:108px">
    <svg width="12" height="14" viewBox="0 0 12 14"><path d="M6 0a5 5 0 0 0-5 5c0 4 5 9 5 9s5-5 5-9a5 5 0 0 0-5-5zm0 7a2 2 0 1 1 0-4 2 2 0 0 1 0 4z" fill="#48a7d3"/></svg>
    <span>Address line here dummy<br>address line here</span>
  </div>
  <div class="contact-line" style="top:152px">
    <svg width="14" height="12" viewBox="0 0 14 12"><path d="M1 3c0-2 3-3 6-3s6 1 6 3v1h-3V3H4v1H1zM3 5h8l2 6H1z" fill="#48a7d3"/></svg>
    <span>(+0100) 555 0142</span>
  </div>
  <div class="contact-line" style="top:190px">
    <svg width="14" height="10" viewBox="0 0 14 10"><rect x="0.5" y="0.5" width="13" height="9" fill="none" stroke="#48a7d3"/><path d="M1 1l6 5 6-5" fill="none" stroke="#48a7d3"/></svg>
    <span>info@serenepath.example</span>
  </div>

  <h4 style="left:720px">About Us</h4>
  <p class="about-text">Lorem ipsum is placeholder text commonly used in the graphic, print, and publishing industries for previewing layouts and visual mockups.</p>
  <div class="subscribe"><span>Email Address</span><b>SUBMIT</b></div>
</footer>

<div class="bottombar">
  <span class="copy">All Rights Reserved. Copyrights @ serenepath 2023</span>
  <div class="social" aria-label="Social links"><span></span><span></span><span></span><span></span><span></span></div>
</div>

</body>
</html>
```